jpg 'poster' for music show to use on social media (only 72dpi needed)

style wanted: Milo Grent goes western

text:

Ray Dunkel
Anna Prescot
Neil Tomasek
Maribeth Oskarsen
... and friends

Friday April 25
Tinbarrel Coffee
Seattle

7:00 PM

$5

would love to get ASAP.

committed to pay for a cool poster!
just need 72 dpi. Thx!

not crazy particular. a cool Milo Grent type layout will be accepted :)

```html
<!DOCTYPE html>
<html lang="en">
<head>
<meta charset="utf-8">
<title>Tinbarrel – Friday, April 25</title>
<link rel="stylesheet" href="https://fonts.googleapis.com/css2?family=Amatic+SC:wght@400;700&family=Wire+One&display=swap">
<style>
  :root {
    --mustard: #e2ae40;
    --paper: #fffdf7;
    --guitar-tone: #eabf62;
  }
  html, body {
    margin: 0;
    padding: 0;
    width: 927px;
    height: 1200px;
    overflow: hidden;
    background: var(--mustard);
  }
  .poster {
    display: block;
    width: 927px;
    height: 1200px;
  }
  .title {
    font-family: "Amatic SC", "Arial Narrow", sans-serif;
    font-weight: 700;
    font-size: 100px;
    letter-spacing: 12px;
    fill: var(--paper);
  }
  .rule { stroke: var(--paper); stroke-width: 4; stroke-linecap: round; }
  .lineup-disc, .price-disc { fill: var(--paper); }
  .lineup-name {
    font-family: "Wire One", "Arial Narrow", sans-serif;
    font-size: 66px;
    letter-spacing: 5px;
    fill: var(--mustard);
  }
  .price {
    font-family: "Wire One", "Arial Narrow", sans-serif;
    font-size: 96px;
    fill: var(--mustard);
  }
  .event-detail {
    font-family: "Amatic SC", "Arial Narrow", sans-serif;
    font-weight: 700;
    font-size: 62px;
    letter-spacing: 1px;
    fill: var(--paper);
  }
  .event-time {
    font-family: "Wire One", "Arial Narrow", sans-serif;
    font-size: 84px;
    letter-spacing: 10px;
    fill: var(--paper);
  }
  .guitar-art { fill: var(--guitar-tone); }
</style>
</head>
<body>
<svg class="poster" viewBox="0 0 927 1200" xmlns="http://www.w3.org/2000/svg">
  <rect width="927" height="1200" fill="var(--mustard)"/>

  <text class="title" x="466" y="129" text-anchor="middle">TINBARREL</text>
  <line class="rule" x1="79" y1="160" x2="833" y2="160"/>
  <line class="rule" x1="144" y1="191" x2="927" y2="191"/>

  <ellipse class="lineup-disc" cx="200" cy="542" rx="380" ry="285"/>
  <g class="lineup">
    <text class="lineup-name" x="33" y="360">RAY DUNKEL</text>
    <text class="lineup-name" x="33" y="459">ANNA PRESCOT</text>
    <text class="lineup-name" x="33" y="557">NEIL TOMASEK</text>
    <text class="lineup-name" x="33" y="654">MARIBETH OSKARSEN</text>
    <text class="lineup-name" x="33" y="753">... AND FRIENDS</text>
  </g>

  <circle class="price-disc" cx="633" cy="348" r="86"/>
  <text class="price" x="633" y="382" text-anchor="middle">$5</text>

  <rect class="guitar-art" x="600" y="455" width="320" height="735" rx="60"
        role="img" aria-label="Line drawing of an acoustic guitar"/>

  <text class="event-detail" x="300" y="947" text-anchor="middle">FRIDAY, APRIL 25</text>
  <text class="event-detail" x="300" y="1030" text-anchor="middle">AT TINBARREL COFFEE</text>
  <text class="event-time" x="300" y="1139" text-anchor="middle">7:00 PM</text>
</svg>
</body>
</html>
```